The name of the company is Dorvane Holdings, LLC. I would like a business card with a logo.

On the top left, I would like a logo design of a crown and I would like Dorvane over the top of the crown while Investments on the bottom. Please see attached files as an example of crown and positioning of Dorvane Holdings. Then I would like the letters DH in the middle(see picture).

Colors

Designer to choose colors to be used in the design.

```html
<!DOCTYPE html>
<html lang="en">
<head>
<meta charset="utf-8">
<title>Dorvane Holdings, LLC — Business Card</title>
<link href="https://fonts.googleapis.com/css2?family=Arvo&family=Lato:wght@400&display=swap" rel="stylesheet">
<style>
  :root {
    --backdrop: #8c4f22;
    --card: #161616;
    --card-shadow: rgba(0, 0, 0, 0.55);
    --accent: #e0594a;
    --gold: #f2b43a;
    --text-light: #d9d9d9;
    --icon-red: #d8342c;
  }
  * { box-sizing: border-box; margin: 0; padding: 0; }
  html, body {
    width: 1200px;
    height: 900px;
    overflow: hidden;
    background: var(--backdrop);
  }
  .stage { position: relative; width: 1200px; height: 900px; }

  .card {
    position: absolute;
    background: var(--card);
    box-shadow: 3px 4px 8px var(--card-shadow);
  }
  .card--front { left: 330px; top: 90px; width: 555px; height: 343px; }
  .card--back  { left: 330px; top: 470px; width: 560px; height: 343px; }

  .brand {
    position: absolute;
    display: flex;
    flex-direction: column;
    align-items: center;
    font-family: "Arvo", serif;
    color: var(--accent);
    white-space: nowrap;
  }
  .brand__dot {
    border-radius: 50%;
    background: var(--gold);
  }
  .card--front .brand { left: 25px; top: 42px; width: 200px; }
  .card--front .brand__dot { width: 76px; height: 76px; margin-bottom: 38px; }
  .card--front .brand__name { font-size: 16px; line-height: 20px; }

  .card--back .brand { left: 0; top: 100px; width: 560px; }
  .card--back .brand__dot { width: 104px; height: 104px; margin-bottom: 44px; }
  .card--back .brand__name { font-size: 21px; line-height: 26px; }

  .holder {
    position: absolute;
    right: 33px;
    top: 58px;
    text-align: right;
  }
  .holder__name {
    font-family: "Arvo", serif;
    font-size: 17px;
    color: var(--accent);
    line-height: 22px;
  }
  .holder__role {
    font-family: "Lato", sans-serif;
    font-size: 15px;
    color: var(--text-light);
    line-height: 20px;
  }

  .address {
    position: absolute;
    left: 25px;
    top: 270px;
    font-family: "Lato", sans-serif;
    font-size: 15.5px;
    line-height: 21px;
    color: var(--text-light);
    font-style: normal;
  }

  .contact {
    position: absolute;
    right: 32px;
    top: 268px;
    list-style: none;
    font-family: "Lato", sans-serif;
    font-size: 15.5px;
    line-height: 21px;
    color: var(--text-light);
    text-align: right;
  }
  .contact__item { display: flex; justify-content: flex-end; align-items: center; gap: 2px; }
  .contact__icon { width: 12px; height: 12px; fill: var(--icon-red); }
</style>
</head>
<body>
<main class="stage">

  <section class="card card--front" aria-label="Card front">
    <div class="brand">
      <span class="brand__dot"></span>
      <span class="brand__name">Dorvane Holdings, LLC</span>
    </div>

    <div class="holder">
      <p class="holder__name">Teodor Vastrelli, MBA</p>
      <p class="holder__role">Founder / CEO</p>
    </div>

    <address class="address">
      418 Larkspur Ridge Road Suite 300<br>
      Cedar Hollow, CA 90361
    </address>

    <ul class="contact">
      <li class="contact__item">(310) 555-0148
        <svg class="contact__icon" viewBox="0 0 12 12" aria-hidden="true">
          <path d="M1 4.5C1 3 2.5 2 6 2s5 1 5 2.5L9.2 5.3 8.5 4H3.5L2.8 5.3Z"/>
          <path d="M3.3 5.5h5.4L10.5 10h-9Z"/>
        </svg>
      </li>
      <li class="contact__item">dorvaneholdings@mailbox.com
        <svg class="contact__icon" viewBox="0 0 12 12" aria-hidden="true">
          <path d="M1 3h10v6.5H1Z"/>
          <path d="M1 3l5 3.6L11 3" fill="none" stroke="#161616" stroke-width="1"/>
        </svg>
      </li>
    </ul>
  </section>

  <section class="card card--back" aria-label="Card back">
    <div class="brand">
      <span class="brand__dot"></span>
      <span class="brand__name">Dorvane Holdings, LLC</span>
    </div>
  </section>

</main>
</body>
</html>
```